Must Be Creative: Trade Show Booth for HR Conference 10x10

Design Style: high-level professional - a bit playful with our theme (read the theme) please be very creative...not boring...eye catching design that will make folks stop and think...We are going for bold. Look at the examples uploaded to this brief. Stick with clean designs professional.

Audience: HR and Talent Leaders

Size 10x10 - (114x91 - safe area 104x81)
we are not doing a podium - do not include it in your design.

Brand: Meridian Growth Studio - do not use our logo in the design. We will decide how and where to add the logo and QR code when we are done with the design. Make sure your design can accommodate a QR Code and our logo.

Brand Colors:
Navy Blue: #003366
Represents: Trust, stability, and professionalism.
Emerald Green: #009473
Represents: Growth, renewal, and prosperity. It also conveys a sense of balance and calm.
Deep Charcoal: #333333
Represents: Sophistication and strength, providing a solid background that makes other colors stand out.
Vibrant Orange: #FF6A00
Represents: Energy, enthusiasm, and warmth. It's an engaging color that can stimulate action and interaction.

FONT: bold face but soft font
Montserrat:
Roboto:
Lato:
Open Sans:

Theme Text:
Are Your Managers Driving Talent Away?
Tagline:
We Empower Leaders to Retain Talent

What we do: (Do not use "What we do text)
(This text can be included or excluded)
Equip Leaders
Engage Teams
Retain Top Talent
Ignite Inclusive Leadership

Imagine Must be Diverse Teams: (See images we uploaded)

Collaborative Teams: An image of a diverse group of professionals engaged in a collaborative work setting. This could be a roundtable discussion or a team actively engaging in a brainstorming session. Such an image would illustrate inclusivity and the dynamic interactions your training promotes.

Empowering Leadership: Consider an image that depicts a leader in action, possibly mentoring or guiding a team member. Showing a moment of teaching or a supportive interaction can powerfully convey the concept of "empower".

Inspirational Settings: An image that includes open, inviting workspace environments that suggest transparency and openness. Spaces that encourage free exchange of ideas can metaphorically represent an inclusive and engaging leadership style.

Success and Achievement: An image that captures a moment of celebration within a team—perhaps cheering or a congratulatory setting—can effectively illustrate the outcome of effective leadership and team retention.

Please ask any questions you have about this project. I've tried to paint the picture as well as I can.

Target Market(s)

HR and Talent Managers

Industry/Entity Type

Human Resources

Font styles to use
Serif
Sans Serif
Decorative

Colors
0054AA
0677BA
7BADD7
CADEEF
E8F1F8
0094D4
00A9DD
6FCCEA
C7EBF8
E9F6FB
00AB8E
00BBA5
67D7C9
C6EFE9
E9F9F6
F0912C
F2A743
F7CA91
FBE8D2
FDF5EE
EB3D1F
EC4F4E
F09395
F8D3D4
FCEDEE

Requirements
Must have
• creative design ideas
Nice to have
• incorporating the photo into the theme
Should not have
• Do not add our logo. We did not include it in the brief - we may add the logo later

```html
<!DOCTYPE html>
<html lang="en">
<head>
<meta charset="utf-8">
<title>Meridian Growth Studio – Booth Backdrop</title>
<link href="https://fonts.googleapis.com/css2?family=Montserrat:wght@500;600;700;800;900&display=swap" rel="stylesheet">
<style>
  :root {
    --stage: #f2f2f2;
    --panel: #ffffff;
    --brand-red: #e01b22;
    --ring-grey: #e3e3e5;
    --navy: #1b2a5c;
    --icon-blue: #0a3fa3;
    --link-blue: #1539a0;
    --ink: #1d1d1f;
    --rule: #7a7a88;
  }
  html, body {
    margin: 0;
    padding: 0;
    width: 1200px;
    height: 2400px;
    overflow: hidden;
    background: var(--stage);
    font-family: "Montserrat", sans-serif;
  }
  .backdrop {
    position: absolute;
    left: 50px;
    top: 650px;
    width: 1100px;
    height: 1100px;
    box-shadow: 0 18px 40px rgba(0,0,0,0.22);
    background: var(--panel);
  }
  .backdrop svg { display: block; width: 100%; height: 100%; }
  .brand-name { font-weight: 800; fill: #fff; font-size: 44px; }
  .question { font-weight: 700; fill: #fff; font-size: 41px; }
  .tagline { font-weight: 900; fill: var(--navy); font-size: 47px; }
  .service-label { font-weight: 700; fill: var(--ink); font-size: 27px; }
  .web-address { font-weight: 700; fill: var(--link-blue); font-size: 29px; letter-spacing: 2px; }
</style>
</head>
<body>
<div class="backdrop">
  <svg viewBox="0 0 1004 1004" xmlns="http://www.w3.org/2000/svg">
    <defs>
      <clipPath id="panel-clip"><rect width="1004" height="1004"/></clipPath>
      <linearGradient id="team-photo-tone" x1="0" y1="0" x2="1" y2="1">
        <stop offset="0" stop-color="#9aa7ae"/>
        <stop offset="0.45" stop-color="#4a5866"/>
        <stop offset="1" stop-color="#2a3340"/>
      </linearGradient>
      <linearGradient id="photo-fade" x1="0" y1="0" x2="0" y2="1">
        <stop offset="0" stop-color="#ffffff" stop-opacity="1"/>
        <stop offset="0.35" stop-color="#ffffff" stop-opacity="0"/>
      </linearGradient>
    </defs>

    <g clip-path="url(#panel-clip)">
      <rect class="panel-bg" width="1004" height="1004" fill="var(--panel)"/>

      <g class="team-photo" role="img" aria-label="Photo of a diverse team of nine business professionals standing with arms crossed in an office lobby">
        <rect x="0" y="520" width="1004" height="390" fill="url(#team-photo-tone)"/>
        <rect x="0" y="520" width="1004" height="390" fill="url(#photo-fade)"/>
      </g>

      <circle class="accent-ring" cx="230" cy="200" r="470" fill="var(--ring-grey)"/>
      <circle class="hero-circle" cx="230" cy="200" r="400" fill="var(--brand-red)"/>

      <g class="brand-block">
        <circle cx="66" cy="108" r="12" fill="#fff"/>
        <text class="brand-name" x="90" y="124">Meridian Growth</text>
        <text class="brand-name" x="90" y="176">Studio</text>
      </g>

      <g class="headline">
        <text class="question" x="48" y="260">Are Your Managers</text>
        <text class="question" x="48" y="312">Driving Talent Away?</text>
      </g>

      <g class="tagline-block">
        <text class="tagline" x="52" y="398">WE EMPOWER</text>
        <text class="tagline" x="52" y="446">LEADERS TO</text>
        <text class="tagline" x="52" y="494" fill="#fff" style="fill:#fff">RETAIN TALENT</text>
      </g>

      <g class="service-rules" stroke="var(--rule)" stroke-width="1.5" stroke-dasharray="4 3">
        <line x1="695" y1="206" x2="1004" y2="206"/>
        <line x1="670" y1="356" x2="1004" y2="356"/>
        <line x1="600" y1="507" x2="1004" y2="507"/>
      </g>

      <g class="service-list">
        <!-- Empower Leaders -->
        <g class="service-item" transform="translate(697,130)">
          <circle r="50" fill="var(--brand-red)"/>
          <circle r="44" fill="#fff"/>
          <circle r="39" fill="var(--icon-blue)"/>
          <g fill="none" stroke="#fff" stroke-width="2">
            <circle cx="0" cy="-4" r="6"/><path d="M-12 14 a12 10 0 0 1 24 0z"/>
            <circle cx="-15" cy="2" r="5"/><circle cx="15" cy="2" r="5"/>
            <path d="M-24 16 a9 8 0 0 1 12 -6 M24 16 a9 8 0 0 0 -12 -6"/>
            <path d="M0 -24 l2 5 5 0 -4 3 2 5 -5 -3 -5 3 2 -5 -4 -3 5 0z"/>
          </g>
        </g>
        <text class="service-label" x="768" y="122">Empower</text>
        <text class="service-label" x="768" y="154">Leaders</text>

        <!-- Engage Teams -->
        <g class="service-item" transform="translate(697,285)">
          <circle r="50" fill="var(--brand-red)"/>
          <circle r="44" fill="#fff"/>
          <circle r="39" fill="var(--icon-blue)"/>
          <g fill="none" stroke="#fff" stroke-width="2">
            <polygon points="0,-22 19,-11 19,11 0,22 -19,11 -19,-11"/>
            <circle cx="0" cy="-3" r="6"/><path d="M-10 12 a10 8 0 0 1 20 0"/>
            <circle cx="0" cy="-22" r="3" fill="#fff"/><circle cx="19" cy="11" r="3" fill="#fff"/><circle cx="-19" cy="11" r="3" fill="#fff"/>
          </g>
        </g>
        <text class="service-label" x="772" y="277">Engage</text>
        <text class="service-label" x="772" y="309">Teams</text>

        <!-- Retain Top Talent -->
        <g class="service-item" transform="translate(652,435)">
          <circle r="50" fill="var(--brand-red)"/>
          <circle r="44" fill="#fff"/>
          <circle r="39" fill="var(--icon-blue)"/>
          <g fill="none" stroke="#fff" stroke-width="2">
            <circle cx="-5" cy="-3" r="13"/><line x1="4" y1="7" x2="16" y2="19" stroke-width="4"/>
            <circle cx="-5" cy="-6" r="4"/><path d="M-12 4 a7 6 0 0 1 14 0"/>
            <path d="M16 -18 l1.5 4 4 0 -3 2.5 1.5 4 -4 -2.5 -4 2.5 1.5 -4 -3 -2.5 4 0z"/>
            <line x1="-20" y1="22" x2="-2" y2="22"/>
          </g>
        </g>
        <text class="service-label" x="733" y="427">Retain Top</text>
        <text class="service-label" x="733" y="459">Talent</text>

        <!-- Inspire Inclusive Leadership -->
        <g class="service-item" transform="translate(568,563)">
          <circle r="50" fill="var(--brand-red)"/>
          <circle r="44" fill="#fff"/>
          <circle r="39" fill="var(--icon-blue)"/>
          <g fill="none" stroke="#fff" stroke-width="2">
            <path d="M-10 4 a12 12 0 1 1 20 0 l-3 6 h-14z"/>
            <line x1="-6" y1="14" x2="6" y2="14"/><line x1="-4" y1="18" x2="4" y2="18"/>
            <ellipse cx="0" cy="-4" rx="24" ry="8" transform="rotate(-25)"/>
            <path d="M-22 -18 l1 3 3 0 -2 2 1 3 -3 -2 -3 2 1 -3 -2 -2 3 0z"/>
            <path d="M20 14 l1 3 3 0 -2 2 1 3 -3 -2 -3 2 1 -3 -2 -2 3 0z"/>
          </g>
        </g>
        <text class="service-label" x="646" y="555">Inspire Inclusive</text>
        <text class="service-label" x="646" y="587">Leadership</text>
      </g>

      <rect class="footer-band" x="0" y="910" width="1004" height="94" fill="var(--panel)"/>
      <text class="web-address" x="502" y="960" text-anchor="middle">www.meridiangrowthstudio.com</text>
    </g>
  </svg>
</div>
</body>
</html>
```